Construction Plant Hire Business Promotional Flyer

I need a promotional flyer / document folder. So an A4 page flyer that can be printed to make an a4 folder that the sales guy can also put his business card into. most of the equipment that i have is excavators, trucks, vacuum excavators, skidsteer loaders and water trucks and trailers. I can also source other equipment to hire out though so i don't want to limit that details to just that equipment. you can view my current brochure online (i don't really like the brochure or the website) to give an idea on the equipment that i have.

Target Market(s)

Construction Industry that requires plant and equipment hire, civil construction industry,

Industry/Entity Type

Business

Contact Information for Business Card

double sided with matte finish and a solid color on the back with logo in reverse and cards to be cut slightly smaller than standard

Number of Pages Required

4 page

Font styles to use
Sans Serif

Colors
0455a3

Requirements
Must have
• similar to other equipment hire companies. tarnlift.com.au, wolbeckhire.com.au and ridgewayhire.com.au
• the company blue color that is on our current website.
• current logo.
• ability to edit website
Nice to have
• photos of construction equipment, simple to read so it does get read when dropped off.
Should not have
• too much text

```html
<!DOCTYPE html>
<html lang="en">
<head>
<meta charset="utf-8">
<title>Ridgeway Hire – Equipment Hire Flyer</title>
<link rel="stylesheet" href="https://fonts.googleapis.com/css2?family=Alfa+Slab+One&family=Roboto+Slab:wght@800&family=Open+Sans:wght@400;700&display=swap">
<style>
  :root {
    --brand-blue: #0455a3;
    --banner-blue: #0d57a8;
    --ink: #3a3a3a;
    --ink-soft: #4a4a4a;
    --callout: #505050;
    --rule: #555555;
    --paper: #ffffff;
    --sky: #b9c6d3;
    --earth: #a8834f;
  }
  * { margin: 0; padding: 0; box-sizing: border-box; }
  html, body { width: 893px; height: 1200px; overflow: hidden; background: var(--paper); }
  .flyer {
    position: relative;
    width: 893px;
    height: 1200px;
    background: var(--paper);
    font-family: "Open Sans", sans-serif;
    color: var(--ink);
  }
  .brand-name {
    position: absolute;
    left: 47px;
    top: 44px;
    font-family: "Alfa Slab One", serif;
    font-size: 44px;
    line-height: 1.12;
    color: var(--brand-blue);
  }
  .contact {
    position: absolute;
    right: 58px;
    top: 54px;
    text-align: right;
    font-style: normal;
    font-weight: 700;
    font-size: 20px;
    line-height: 26px;
    letter-spacing: 0.8px;
    color: var(--ink);
  }
  .rule-blue {
    position: absolute;
    left: 0; right: 0;
    top: 180px;
    height: 7px;
    border-top: 2px solid var(--brand-blue);
    border-bottom: 2px solid var(--brand-blue);
  }
  .rule-dots {
    position: absolute;
    left: 0; right: 0;
    border-top: 4px dotted var(--rule);
  }
  .rule-dots.top { top: 198px; }
  .rule-dots.mid { top: 636px; }
  .rule-dots.text { top: 900px; left: 47px; right: 58px; }
  .rule-dots.foot { top: 1102px; }
  .hero-photo {
    position: absolute;
    left: 0; right: 0;
    top: 209px;
    height: 416px;
    background: linear-gradient(180deg, var(--sky) 0%, #d6dde4 45%, #c7a46c 68%, var(--earth) 100%);
  }
  .cta-banner {
    position: absolute;
    left: 48px;
    top: 664px;
    width: 787px;
    height: 100px;
    background: var(--banner-blue);
    box-shadow: 2px 3px 5px rgba(0,0,0,0.25);
  }
  .cta-banner svg { position: absolute; left: 26px; top: 20px; }
  .cta-banner h1 {
    position: absolute;
    left: 184px;
    top: 9px;
    font-family: "Alfa Slab One", serif;
    font-weight: 400;
    font-size: 36px;
    line-height: 42px;
    color: #ffffff;
    text-shadow: 2px 2px 0 rgba(0,0,0,0.25);
    white-space: nowrap;
  }
  .section-title {
    position: absolute;
    left: 62px;
    top: 790px;
    font-family: "Roboto Slab", serif;
    font-weight: 800;
    font-size: 33px;
    line-height: 46px;
    color: var(--ink-soft);
    text-shadow: 2px 2px 0 rgba(0,0,0,0.15);
  }
  .section-title span { display: block; padding-left: 12px; }
  .callout {
    position: absolute;
    left: 433px;
    top: 793px;
    width: 390px;
    height: 80px;
    background: var(--callout);
    color: #ffffff;
    font-size: 14.5px;
    line-height: 21px;
    padding: 8px 14px 0 27px;
  }
  .callout::before {
    content: "";
    position: absolute;
    left: -13px;
    top: 26px;
    border-top: 13px solid transparent;
    border-bottom: 13px solid transparent;
    border-right: 13px solid var(--callout);
  }
  .pointer-arrow { position: absolute; left: 36px; top: 922px; }
  .body-copy {
    position: absolute;
    left: 82px;
    top: 920px;
    width: 712px;
    font-size: 17px;
    line-height: 31px;
    color: var(--ink-soft);
  }
  .service-area {
    position: absolute;
    left: 0; right: 0;
    top: 1040px;
    text-align: center;
    font-family: "Alfa Slab One", serif;
    font-size: 34px;
    color: var(--brand-blue);
    text-shadow: 2px 3px 0 rgba(0,0,0,0.18);
  }
  .footer {
    position: absolute;
    left: 0; right: 0;
    top: 1114px;
    bottom: 0;
    background: var(--banner-blue);
    display: flex;
    align-items: center;
    justify-content: center;
    color: #ffffff;
    font-weight: 700;
    font-size: 20px;
    letter-spacing: 0.8px;
  }
</style>
</head>
<body>
<main class="flyer">
  <header>
    <div class="brand-name">RIDGEWAY<br>HIRE</div>
    <address class="contact">
      (07) 5550 1842<br>
      ridgewayhire.com.au<br>
      plant@ridgewayhire.com.au
    </address>
  </header>

  <div class="rule-blue"></div>
  <div class="rule-dots top"></div>

  <div class="hero-photo" role="img" aria-label="Photo of an excavator with a raised bucket on a mound of dug earth under a cloudy sky"></div>

  <div class="rule-dots mid"></div>

  <section class="cta-banner">
    <svg width="100" height="62" viewBox="0 0 100 62" aria-hidden="true">
      <path d="M4 20 C4 6 96 6 96 20 L96 26 L74 26 L74 18 C60 14 40 14 26 18 L26 26 L4 26 Z" fill="#ffffff"/>
      <path d="M28 28 L72 28 L88 56 L12 56 Z" fill="#ffffff"/>
      <circle cx="50" cy="42" r="9" fill="var(--banner-blue)"/>
      <circle cx="50" cy="42" r="4" fill="#ffffff"/>
    </svg>
    <h1>HIRE LIKE A PRO,<br>CALL 1800 RIDGE HIRE</h1>
  </section>

  <h2 class="section-title">Equipment<span>Hire</span></h2>

  <p class="callout">Ridgeway Hire specialise in plant equipment hire solutions for the civil, construction and mining industries throughout Queensland.</p>

  <div class="rule-dots text"></div>

  <svg class="pointer-arrow" width="40" height="52" viewBox="0 0 40 52" aria-hidden="true">
    <path d="M18 3 C6 12 6 30 22 42" fill="none" stroke="#444" stroke-width="2"/>
    <path d="M13 43 L26 46 L22 33 Z" fill="#444"/>
  </svg>

  <p class="body-copy">When you need equipment operated on location in Queensland, that could mean you are in town, on the beach, in a rainforest jungle or miles from anywhere . . . way outback. You need reliable equipment and a fast response supplier, so you don’t suffer downtime.</p>

  <p class="service-area">Servicing all of Queensland</p>

  <div class="rule-dots foot"></div>

  <footer class="footer">ridgewayhire.com.au</footer>
</main>
</body>
</html>
```